Business Card Design Project

I need a new business card design for my building/development company: Ridgewell Constructions.

We specialise in small sub-divisions, multi-story developments and new house builds.
We handle the whole process from concept stage right throught to a fully developed property.
Updates

Project Deadline Extended
Reason: Need a couple of extra days to decide as there are so many amazing designs

Target Market(s)

people looking to develop their property and need help. New property buyers

Industry/Entity Type

House

Requirements
Must have
• My logo on both sides:
Side 1: Logo taking up whole side as per old card but with a color/style change.

Side 2: Contact page: include logo but the rest just surprise me!

All contact details will be: (and need to be changable for each employee) I'll inform you of specifics before printing.

Name Surname
Position ie. Managing director
M: insert mobile
E: insert email
P.O. Box 518, Elmhurst, Vic, 3145
www.ridgewellconstructions.com.au

Nice to have
• Colors i'd like: (not necessarily all but this is the basic idea)

Black, blue, grey, silver, white

```html
<!DOCTYPE html>
<html lang="en">
<head>
<meta charset="utf-8">
<title>Ridgewell Constructions – Business Card</title>
<link href="https://fonts.googleapis.com/css2?family=Source+Sans+3:ital,wght@0,300;0,400;0,600;0,700;1,400&display=swap" rel="stylesheet">
<style>
  :root {
    --backdrop: #e9ecef;
    --card: #ffffff;
    --brand-blue: #1a8fd6;
    --panel-blue: #1f9ae0;
    --panel-edge: #8a939b;
    --ink: #2b2b2b;
    --white: #ffffff;
  }
  * { box-sizing: border-box; margin: 0; padding: 0; }
  html, body {
    width: 1200px; height: 800px; overflow: hidden;
    background: var(--backdrop);
    font-family: "Source Sans 3", Arial, sans-serif;
  }
  .canvas { position: relative; width: 1200px; height: 800px; }
  .card {
    position: absolute; left: 100px; top: 114px;
    width: 1000px; height: 572px;
    background: var(--card);
    box-shadow: 0 10px 30px rgba(0,0,0,.15);
    overflow: hidden;
  }
  .brand-mark {
    position: absolute; left: 470px; top: 48px;
    width: 64px; height: 64px;
    background: var(--brand-blue);
  }
  .brand {
    position: absolute; left: 0; right: 0; top: 128px;
    text-align: center;
  }
  .brand-name {
    font-weight: 700; font-size: 54px; line-height: 1;
    color: var(--brand-blue); letter-spacing: -0.5px;
  }
  .brand-tagline {
    margin-top: 6px;
    font-size: 21px; color: var(--ink); letter-spacing: 0.5px;
  }
  .website {
    margin-top: 10px;
    font-size: 24px; color: var(--brand-blue); font-weight: 400;
  }
  .contact-panel {
    position: absolute; left: 26px; right: 0; top: 312px; bottom: 0;
    background: var(--panel-blue);
    border-top-left-radius: 64px;
    box-shadow: inset 3px 5px 6px rgba(0,0,0,.25), -2px -2px 0 var(--panel-edge);
  }
  .person {
    position: absolute; left: 46px; top: 118px; color: var(--white);
  }
  .person-name { font-size: 46px; font-weight: 400; letter-spacing: 1px; line-height: 1.05; }
  .person-role { font-size: 25px; font-weight: 300; margin-top: 6px; }
  .details {
    position: absolute; right: 44px; top: 26px;
    list-style: none; color: var(--white);
    font-size: 23px; font-weight: 300; text-align: right;
  }
  .details li {
    display: flex; align-items: center; justify-content: flex-end;
    gap: 10px; line-height: 1.35;
  }
  .details li.phone { margin-bottom: 34px; }
  .details svg { width: 24px; height: 24px; flex: none; }
</style>
</head>
<body>
<div class="canvas">
  <section class="card" aria-label="Ridgewell Constructions business card">
    <div class="brand-mark" aria-hidden="true"></div>
    <header class="brand">
      <h1 class="brand-name">Ridgewell Constructions</h1>
      <p class="brand-tagline">renovation-construction-development</p>
      <p class="website">www.ridgewellconstructions.com.au</p>
    </header>

    <div class="contact-panel">
      <div class="person">
        <p class="person-name">Marcus Hale</p>
        <p class="person-role">Managing Director</p>
      </div>
      <ul class="details">
        <li class="phone">
          <svg viewBox="0 0 24 24" aria-hidden="true"><rect x="6" y="2" width="12" height="20" rx="2" fill="none" stroke="#fff" stroke-width="1.6"/><line x1="10" y1="18.5" x2="14" y2="18.5" stroke="#fff" stroke-width="1.6"/></svg>
          0400.555.019
        </li>
        <li class="email">
          <svg viewBox="0 0 24 24" aria-hidden="true"><rect x="2" y="5" width="20" height="14" fill="#fff"/><path d="M2 5l10 8 10-8" fill="none" stroke="#1f9ae0" stroke-width="1.6"/></svg>
          marcus@ridgewellconstructions.com
        </li>
        <li class="address">
          <svg viewBox="0 0 24 24" aria-hidden="true"><rect x="3" y="3" width="11" height="19" fill="#fff"/><rect x="14" y="9" width="7" height="13" fill="#fff"/><g fill="#1f9ae0"><rect x="5" y="5" width="2.5" height="2.5"/><rect x="9.5" y="5" width="2.5" height="2.5"/><rect x="5" y="10" width="2.5" height="2.5"/><rect x="9.5" y="10" width="2.5" height="2.5"/><rect x="5" y="15" width="2.5" height="2.5"/><rect x="9.5" y="15" width="2.5" height="2.5"/><rect x="16" y="12" width="3" height="2.5"/><rect x="16" y="17" width="3" height="2.5"/></g></svg>
          P.O. Box 518, Elmhurst, Vic, 3145
        </li>
      </ul>
    </div>
  </section>
</div>
</body>
</html>
```